Label Design for Amber Reed Specialty Coffee Roasters

We are a specialty coffee beans Roasting Shop named "Amber Reed". We pack our beans in stand up poaches of varying sizes. We sell beans both to B2C and B2B and are looking to design stickers that will stand out. Our logo was designed with a black and white background. So far, we have been using white glossy bean bags and came up with a front label design that we would like to use for our labels.
We would like to see the design tweaked to fit both a white bag and a black one.
Currently, the attached front label design does not work on white bags. We would also like to have a back sticker designed that needs to include: 1- a description section for the type of beans used 2- a QR code section

Target Market(s)

Specialty beans in our area are typically liked by the younger generations 40 years and younger. Both male and females drink our coffee with varying income levels. But generally, middle class and above buy our coffee beans.

Requirements
Must have
• We are am looking for a sticker to be placed on a coffee bean bag. The sticker needs to contain the roasting shop's logo and brand name "Amber Reed". Also, the sticker needs to have the following: country name, bean variety, weight (kg), roast date. The sticker needs to have the following specifications on a 5 point Likert scale (Strength, Fruitiness, Earthiness, Brightness). I uploaded a front label design that needs to be tweaked to fit both a white bag and a black one. The current design has owls representing the 5 point Likert scale and part of the shop's logo. We would like to keep that part of the design if possible. Currently, the attached front label design does not work on white bags.
We would also like to have a back sticker designed that needs to include: 1- a description section for the type of beans used 2- a QR code section
Nice to have
• The font that is used in the logo is League Gothic. It is okay to use this font or any other font if you find it more appropriate for the design.

```html
<!DOCTYPE html>
<html lang="en">
<head>
<meta charset="utf-8">
<title>Amber Reed Specialty Coffee Roasters – Front Labels</title>
<link href="https://fonts.googleapis.com/css2?family=Encode+Sans+Condensed:wght@400;600;700&display=swap" rel="stylesheet">
<style>
  :root {
    --page: #ececea;
    --ink: #3a2e27;
    --cream: #f3ead5;
    --cream-soft: #f7f0df;
    --sage: #9dc4b1;
    --sage-panel: #8fbea6;
    --sage-art: #86b39c;
    --umber: #7b6958;
    --umber-panel: #c6b89f;
    --umber-art: #6c5a4a;
    --dot-empty: #f3ead5;
  }
  * { box-sizing: border-box; margin: 0; padding: 0; }
  html, body { width: 903px; height: 1200px; overflow: hidden; }
  body {
    background: var(--page);
    font-family: "Encode Sans Condensed", "Arial Narrow", sans-serif;
    color: var(--ink);
    position: relative;
  }
  .label {
    position: absolute;
    width: 236px;
    height: 283px;
    overflow: hidden;
    background: var(--label-bg);
  }
  .label--sage { --label-bg: var(--sage); --panel-bg: var(--sage-panel); --art: var(--sage-art); }
  .label--umber { --label-bg: var(--umber); --panel-bg: var(--umber-panel); --art: var(--umber-art); }
  .label--a { left: 108px; top: 204px; }
  .label--b { left: 565px; top: 204px; }
  .label--c { left: 108px; top: 798px; }
  .label--d { left: 565px; top: 798px; }

  .label__artwork {
    position: absolute; inset: 0;
    background:
      radial-gradient(ellipse 60px 50px at 30px 60px, var(--art), transparent 70%),
      radial-gradient(ellipse 70px 90px at 210px 80px, var(--art), transparent 70%),
      radial-gradient(ellipse 60px 80px at 10px 220px, var(--art), transparent 70%);
  }
  .label__sheen { position: absolute; inset: 0; width: 236px; height: 283px; }

  .brand-badge {
    position: absolute;
    left: 74px; top: 15px;
    width: 88px; height: 64px;
    background: var(--cream);
    border-radius: 8px;
    display: flex; align-items: center; justify-content: center; gap: 5px;
  }
  .brand-badge__dot { width: 8px; height: 8px; border-radius: 50%; background: var(--ink); }
  .brand-badge__name {
    font-weight: 700; font-size: 14px; line-height: 1;
    text-transform: uppercase; color: var(--ink);
  }

  .info-card {
    position: absolute;
    left: 20px; top: 91px;
    width: 197px; height: 175px;
    background: var(--cream);
    border-radius: 10px;
    text-align: center;
  }
  .info-card__rule {
    position: absolute; left: 8px; right: 8px; height: 0;
    border-top: 1.5px dotted var(--panel-bg);
  }
  .info-card__rule--top { top: 10px; }
  .info-card__rule--bottom { top: 165px; }
  .origin { position: absolute; left: 0; right: 0; top: 17px; font-weight: 700; font-size: 14px; line-height: 1; }
  .variety { position: absolute; left: 0; right: 0; top: 33px; font-size: 11px; line-height: 1; }

  .profile {
    position: absolute; left: 29px; top: 51px;
    width: 137px; height: 70px;
    background: var(--panel-bg);
    border-radius: 10px;
    padding-top: 7px;
  }
  .profile__row { display: flex; align-items: center; height: 14px; }
  .profile__name { width: 64px; text-align: right; font-size: 10px; line-height: 1; padding-right: 6px; }
  .profile__scale { display: flex; gap: 2px; }
  .profile__mark { width: 7px; height: 7px; border-radius: 50%; background: var(--ink); }
  .profile__mark--empty { background: var(--dot-empty); }

  .facts {
    position: absolute; left: 0; right: 0; top: 131px;
    display: flex; justify-content: center;
    font-size: 10px; line-height: 13px;
  }
  .facts__item { padding: 0 7px; }
  .facts__item + .facts__item { border-left: 1.5px dotted var(--panel-bg); }
  .facts__value { font-weight: 400; }
  .label--umber .facts__value { font-weight: 600; }
</style>
</head>
<body>

<!-- Sage edition, shown twice for black and white bags -->
<section class="label label--sage label--a">
  <div class="label__artwork" role="img" aria-label="Line illustration of a coffee cup, beans and coffee plant branches"></div>
  <svg class="label__sheen" viewBox="0 0 236 283" aria-hidden="true"><path d="M0 0 H40 C10 80 10 200 60 283 H0 Z" fill="#ffffff" opacity=".18"/><path d="M236 0 H210 C240 90 190 180 236 283 Z" fill="#000000" opacity=".05"/></svg>
  <div class="brand-badge"><span class="brand-badge__dot"></span><span class="brand-badge__name">Amber Reed</span></div>
  <div class="info-card">
    <div class="info-card__rule info-card__rule--top"></div>
    <p class="origin">COLOMBIA</p>
    <p class="variety">VARIETY</p>
    <div class="profile">
      <div class="profile__row"><span class="profile__name">STRENGHT</span><span class="profile__scale"><i class="profile__mark"></i><i class="profile__mark"></i><i class="profile__mark"></i><i class="profile__mark profile__mark--empty"></i><i class="profile__mark profile__mark--empty"></i></span></div>
      <div class="profile__row"><span class="profile__name">FRUITINESS</span><span class="profile__scale"><i class="profile__mark"></i><i class="profile__mark profile__mark--empty"></i><i class="profile__mark profile__mark--empty"></i><i class="profile__mark profile__mark--empty"></i><i class="profile__mark profile__mark--empty"></i></span></div>
      <div class="profile__row"><span class="profile__name">EARTHINESS</span><span class="profile__scale"><i class="profile__mark"></i><i class="profile__mark"></i><i class="profile__mark"></i><i class="profile__mark profile__mark--empty"></i><i class="profile__mark profile__mark--empty"></i></span></div>
      <div class="profile__row"><span class="profile__name">BRIGHTNESS</span><span class="profile__scale"><i class="profile__mark"></i><i class="profile__mark"></i><i class="profile__mark"></i><i class="profile__mark profile__mark--empty"></i><i class="profile__mark profile__mark--empty"></i></span></div>
    </div>
    <div class="facts">
      <div class="facts__item">WEIGHT<br><span class="facts__value">60 KG</span></div>
      <div class="facts__item">ROAST DATE<br><span class="facts__value">05/5/2021</span></div>
    </div>
    <div class="info-card__rule info-card__rule--bottom"></div>
  </div>
</section>

<section class="label label--sage label--b">
  <div class="label__artwork" role="img" aria-label="Line illustration of a coffee cup, beans and coffee plant branches"></div>
  <svg class="label__sheen" viewBox="0 0 236 283" aria-hidden="true"><path d="M0 0 H40 C10 80 10 200 60 283 H0 Z" fill="#ffffff" opacity=".18"/><path d="M236 0 H210 C240 90 190 180 236 283 Z" fill="#000000" opacity=".05"/></svg>
  <div class="brand-badge"><span class="brand-badge__dot"></span><span class="brand-badge__name">Amber Reed</span></div>
  <div class="info-card">
    <div class="info-card__rule info-card__rule--top"></div>
    <p class="origin">COLOMBIA</p>
    <p class="variety">VARIETY</p>
    <div class="profile">
      <div class="profile__row"><span class="profile__name">STRENGHT</span><span class="profile__scale"><i class="profile__mark"></i><i class="profile__mark"></i><i class="profile__mark"></i><i class="profile__mark profile__mark--empty"></i><i class="profile__mark profile__mark--empty"></i></span></div>
      <div class="profile__row"><span class="profile__name">FRUITINESS</span><span class="profile__scale"><i class="profile__mark"></i><i class="profile__mark profile__mark--empty"></i><i class="profile__mark profile__mark--empty"></i><i class="profile__mark profile__mark--empty"></i><i class="profile__mark profile__mark--empty"></i></span></div>
      <div class="profile__row"><span class="profile__name">EARTHINESS</span><span class="profile__scale"><i class="profile__mark"></i><i class="profile__mark"></i><i class="profile__mark"></i><i class="profile__mark profile__mark--empty"></i><i class="profile__mark profile__mark--empty"></i></span></div>
      <div class="profile__row"><span class="profile__name">BRIGHTNESS</span><span class="profile__scale"><i class="profile__mark"></i><i class="profile__mark"></i><i class="profile__mark"></i><i class="profile__mark profile__mark--empty"></i><i class="profile__mark profile__mark--empty"></i></span></div>
    </div>
    <div class="facts">
      <div class="facts__item">WEIGHT<br><span class="facts__value">60 KG</span></div>
      <div class="facts__item">ROAST DATE<br><span class="facts__value">05/5/2021</span></div>
    </div>
    <div class="info-card__rule info-card__rule--bottom"></div>
  </div>
</section>

<!-- Umber edition -->
<section class="label label--umber label--c">
  <div class="label__artwork" role="img" aria-label="Line illustration of a coffee cup, beans and coffee plant branches"></div>
  <svg class="label__sheen" viewBox="0 0 236 283" aria-hidden="true"><path d="M0 0 H40 C10 80 10 200 60 283 H0 Z" fill="#ffffff" opacity=".18"/><path d="M236 0 H210 C240 90 190 180 236 283 Z" fill="#000000" opacity=".05"/></svg>
  <div class="brand-badge"><span class="brand-badge__dot"></span><span class="brand-badge__name">Amber Reed</span></div>
  <div class="info-card">
    <div class="info-card__rule info-card__rule--top"></div>
    <p class="origin">COLOMBIA</p>
    <p class="variety">VARIETY</p>
    <div class="profile">
      <div class="profile__row"><span class="profile__name">STRENGHT</span><span class="profile__scale"><i class="profile__mark"></i><i class="profile__mark"></i><i class="profile__mark"></i><i class="profile__mark profile__mark--empty"></i><i class="profile__mark profile__mark--empty"></i></span></div>
      <div class="profile__row"><span class="profile__name">FRUITINESS</span><span class="profile__scale"><i class="profile__mark"></i><i class="profile__mark profile__mark--empty"></i><i class="profile__mark profile__mark--empty"></i><i class="profile__mark profile__mark--empty"></i><i class="profile__mark profile__mark--empty"></i></span></div>
      <div class="profile__row"><span class="profile__name">EARTHINESS</span><span class="profile__scale"><i class="profile__mark"></i><i class="profile__mark"></i><i class="profile__mark"></i><i class="profile__mark profile__mark--empty"></i><i class="profile__mark profile__mark--empty"></i></span></div>
      <div class="profile__row"><span class="profile__name">BRIGHTNESS</span><span class="profile__scale"><i class="profile__mark"></i><i class="profile__mark"></i><i class="profile__mark"></i><i class="profile__mark profile__mark--empty"></i><i class="profile__mark profile__mark--empty"></i></span></div>
    </div>
    <div class="facts">
      <div class="facts__item">WEIGHT<br><span class="facts__value">60 KG</span></div>
      <div class="facts__item">ROAST DATE<br><span class="facts__value">05/5/2021</span></div>
    </div>
    <div class="info-card__rule info-card__rule--bottom"></div>
  </div>
</section>

<section class="label label--umber label--d">
  <div class="label__artwork" role="img" aria-label="Line illustration of a coffee cup, beans and coffee plant branches"></div>
  <svg class="label__sheen" viewBox="0 0 236 283" aria-hidden="true"><path d="M0 0 H40 C10 80 10 200 60 283 H0 Z" fill="#ffffff" opacity=".18"/><path d="M236 0 H210 C240 90 190 180 236 283 Z" fill="#000000" opacity=".05"/></svg>
  <div class="brand-badge"><span class="brand-badge__dot"></span><span class="brand-badge__name">Amber Reed</span></div>
  <div class="info-card">
    <div class="info-card__rule info-card__rule--top"></div>
    <p class="origin">COLOMBIA</p>
    <p class="variety">VARIETY</p>
    <div class="profile">
      <div class="profile__row"><span class="profile__name">STRENGHT</span><span class="profile__scale"><i class="profile__mark"></i><i class="profile__mark"></i><i class="profile__mark"></i><i class="profile__mark profile__mark--empty"></i><i class="profile__mark profile__mark--empty"></i></span></div>
      <div class="profile__row"><span class="profile__name">FRUITINESS</span><span class="profile__scale"><i class="profile__mark"></i><i class="profile__mark profile__mark--empty"></i><i class="profile__mark profile__mark--empty"></i><i class="profile__mark profile__mark--empty"></i><i class="profile__mark profile__mark--empty"></i></span></div>
      <div class="profile__row"><span class="profile__name">EARTHINESS</span><span class="profile__scale"><i class="profile__mark"></i><i class="profile__mark"></i><i class="profile__mark"></i><i class="profile__mark profile__mark--empty"></i><i class="profile__mark profile__mark--empty"></i></span></div>
      <div class="profile__row"><span class="profile__name">BRIGHTNESS</span><span class="profile__scale"><i class="profile__mark"></i><i class="profile__mark"></i><i class="profile__mark"></i><i class="profile__mark profile__mark--empty"></i><i class="profile__mark profile__mark--empty"></i></span></div>
    </div>
    <div class="facts">
      <div class="facts__item">WEIGHT<br><span class="facts__value">60 KG</span></div>
      <div class="facts__item">ROAST DATE<br><span class="facts__value">05/5/2021</span></div>
    </div>
    <div class="info-card__rule info-card__rule--bottom"></div>
  </div>
</section>

</body>
</html>
```